Popup Banners - BrightCounsel - Legal Technology

- We need two banners (same style) designed with two different images and different text.

- The details of the printing requirements are attached, along with suggested images.

- The banners should share the same theme as our website www.brightcounsel.com.au

- The first banner would include our logo (attached), use the 'roads join' image (attached) in some way and text: New Opportunities - Where legal services and technology meet.

- The second banner would include our logo (attached), use the 'jigsaw' image (attached) in some way and use text: Legal Technology Strategy, Advice and Capability.

- Details on what are required from the Printer is attached also.

Target Market(s)

Legal Professionals

Industry/Entity Type

Information Technology

Font styles to use
Sans Serif

Requirements
Must have
• Our logo (attached), suggested text and the image mentioned for each.
Nice to have
• Professional and modern look
Should not have
• Cheap looking

```html
<!DOCTYPE html>
<html lang="en">
<head>
<meta charset="utf-8">
<title>BrightCounsel – Legal Technology Strategy, Advice and Capability</title>
<link rel="stylesheet" href="https://fonts.googleapis.com/css2?family=Barlow:wght@500;600&family=Barlow+Semi+Condensed:wght@500;600&display=swap">
<style>
  :root {
    --silver-light: #f4f4f5;
    --silver-mid: #d9d9dc;
    --gold: #b8862b;
    --gold-light: #dcae52;
    --purple: #5b2a86;
    --violet: #3a2a78;
    --navy: #14204a;
    --teal-dark: #12303f;
    --charcoal: #1e1e1f;
    --charcoal-deep: #0f0f10;
    --ink: #3a3a3c;
    --white: #ffffff;
  }
  html, body {
    margin: 0;
    padding: 0;
    width: 1200px;
    height: 2963px;
    overflow: hidden;
    background: var(--white);
  }
  .banner {
    position: relative;
    width: 1200px;
    height: 2963px;
    overflow: hidden;
    background: linear-gradient(180deg, var(--purple) 0%, var(--violet) 30%, var(--navy) 60%, var(--teal-dark) 80%, var(--navy) 100%);
    font-family: "Barlow Semi Condensed", "Barlow", sans-serif;
  }
  .banner__photo {
    position: absolute;
    left: 0;
    top: 1650px;
    width: 1200px;
    height: 850px;
    background:
      radial-gradient(ellipse 260px 200px at 620px 520px, rgba(220, 235, 250, 0.85), rgba(120, 160, 200, 0.25) 60%, transparent 100%),
      linear-gradient(180deg, rgba(20, 32, 74, 0) 0%, rgba(25, 60, 90, 0.7) 45%, rgba(20, 40, 70, 0.9) 100%);
  }
  .shapes {
    position: absolute;
    inset: 0;
    width: 1200px;
    height: 2963px;
  }
  .brand {
    position: absolute;
    top: 190px;
    left: 0;
    width: 1200px;
    display: flex;
    justify-content: center;
    align-items: center;
    gap: 36px;
  }
  .brand__mark {
    width: 84px;
    height: 84px;
    background: var(--ink);
  }
  .brand__name {
    font-family: "Barlow", sans-serif;
    font-weight: 500;
    font-size: 78px;
    letter-spacing: 14px;
    color: var(--ink);
    line-height: 1;
  }
  .headline {
    position: absolute;
    top: 880px;
    left: 0;
    width: 1200px;
    margin: 0;
    text-align: center;
    color: var(--white);
    font-weight: 500;
    font-size: 74px;
    line-height: 150px;
    letter-spacing: 1px;
    text-transform: uppercase;
  }
  .headline span { display: block; }
  .address {
    position: absolute;
    top: 2752px;
    left: 0;
    width: 1200px;
    margin: 0;
    text-align: center;
    color: var(--white);
    font-weight: 600;
    font-size: 32px;
    letter-spacing: 1.5px;
    text-transform: uppercase;
  }
</style>
</head>
<body>
<main class="banner">
  <div class="banner__photo" role="img" aria-label="Photo of a hand placing a glowing jigsaw piece into a puzzle, with soft blue light and bokeh"></div>

  <svg class="shapes" viewBox="0 0 1200 2963" aria-hidden="true">
    <defs>
      <linearGradient id="silverFill" x1="0" y1="0" x2="0" y2="1">
        <stop offset="0" stop-color="var(--silver-mid)"/>
        <stop offset="1" stop-color="var(--silver-light)"/>
      </linearGradient>
      <linearGradient id="goldFill" x1="0" y1="0" x2="1" y2="0">
        <stop offset="0" stop-color="var(--gold)"/>
        <stop offset="0.5" stop-color="var(--gold-light)"/>
        <stop offset="1" stop-color="var(--gold)"/>
      </linearGradient>
      <linearGradient id="charcoalFill" x1="0" y1="0" x2="0" y2="1">
        <stop offset="0" stop-color="var(--charcoal)"/>
        <stop offset="1" stop-color="var(--charcoal-deep)"/>
      </linearGradient>
    </defs>
    <polygon class="header-gold" points="0,400 270,560 1200,330 1200,395 270,605 0,450" fill="url(#goldFill)"/>
    <polygon class="header-panel" points="0,0 1200,0 1200,340 270,530 0,375" fill="url(#silverFill)"/>
    <polygon class="footer-gold" points="0,2520 815,2350 1200,2440 1200,2500 815,2400 0,2580" fill="url(#goldFill)"/>
    <polygon class="footer-panel" points="0,2580 815,2405 1200,2495 1200,2963 0,2963" fill="url(#charcoalFill)"/>
  </svg>

  <div class="brand">
    <div class="brand__mark"></div>
    <div class="brand__name">BrightCounsel</div>
  </div>

  <h1 class="headline">
    <span>Legal</span>
    <span>Technology Strategy,</span>
    <span>Advice</span>
    <span>and</span>
    <span>Capability</span>
  </h1>

  <p class="address">Level 12, 48 Harbour Street Brisbane QLD, Australia</p>
</main>
</body>
</html>
```